Veloran Ceramic Coating Flyer

We are an automotive ceramic coating company. We install protective coatings on supercars/exotics/luxury cars. We have dealerships that sell our coatings in house. This flyer is to be branded alongside Osprey/Trail Voyager. A very poor mock flyer has been attached. A maintenance guide has also been attached for context, however washing procedures are not to be included in the flyer. The flyer is to be a two page (Front and back). It is to showcase the properties of the coatings, and their attributes. They will be placed in front of displays at the dealerships. We would like our coating tiers included in the flyer, 1.5, 3, 5, 10 year. With labor hour estimates below each to create context. See website for an example: www.veloranluxe.ca
PLEASE integrate pictures of aircraft, as attached into the document.
Thank you so much!

Target Market(s)

Walk in clients within dealerships.

Logo Text

Please update logo look and feel. We feel that the logo looks dated. Looking for depth. A luxurious feel.

```html
<!DOCTYPE html>
<html lang="en">
<head>
<meta charset="utf-8">
<title>Veloran Ceramic Coating Flyer</title>
<link rel="stylesheet" href="https://fonts.googleapis.com/css2?family=Oswald:wght@400;500;700&family=Roboto+Condensed:wght@400;700&display=swap">
<style>
:root{
  --stage:#d9dadb;
  --paper:#ffffff;
  --red:#d3102a;
  --red-deep:#8e0a1c;
  --ink:#151515;
  --charcoal:#232427;
  --grey:#6b6d72;
  --blue:#1f4fa8;
}
*{margin:0;padding:0;box-sizing:border-box}
html,body{width:878px;height:1200px;overflow:hidden;background:var(--stage)}
body{position:relative;font-family:"Roboto Condensed",sans-serif;color:var(--ink)}
.page{position:absolute;top:306px;width:415px;height:587px;background:var(--paper);overflow:hidden;box-shadow:0 4px 14px rgba(0,0,0,.25)}
.page--front{left:16px}
.page--back{left:447px}
.photo{position:absolute}
.title{font-family:"Oswald",sans-serif;font-weight:700;text-transform:uppercase;line-height:1.05}

/* front */
.front-hero-red{left:0;top:0;width:230px;height:330px;background:linear-gradient(135deg,#5a0710,#c8142b 55%,#ff4858);clip-path:polygon(0 0,100% 0,62% 100%,0 100%)}
.front-hero-blue{left:150px;top:0;width:265px;height:250px;background:linear-gradient(160deg,#0c1c3d,#2f6ad0 55%,#0b1326);clip-path:polygon(30% 0,100% 0,100% 100%,0 100%)}
.front-stripe{left:130px;top:0;width:40px;height:340px;background:var(--charcoal);transform:skewX(-17deg)}
.front-band{position:absolute;left:-10px;top:318px;width:300px;height:58px;background:var(--red);clip-path:polygon(0 0,100% 0,88% 100%,0 100%)}
.front-band .title{position:absolute;left:24px;top:8px;color:#fff;font-size:19px;width:240px}
.pill{position:absolute;left:16px;height:19px;padding:0 10px;background:var(--red);color:#fff;font-family:"Oswald",sans-serif;font-weight:500;font-size:11px;line-height:19px;letter-spacing:.5px;text-transform:uppercase}
.tiers-head{position:absolute;left:16px;top:444px;color:var(--red);font-size:17px}
.tier-list{position:absolute;left:16px;top:468px;width:170px;list-style:none;display:grid;grid-template-columns:1fr 1fr;gap:3px 10px;font-size:11px;font-weight:700}
.tier-list li::before{content:"";display:inline-block;width:6px;height:6px;background:var(--red);margin-right:5px;vertical-align:1px}
.front-car{left:195px;top:260px;width:220px;height:300px;background:linear-gradient(200deg,#2a2c31,#7d8087 45%,#15161a);clip-path:polygon(30% 0,100% 0,100% 100%,0 100%)}
.logo{position:absolute;display:flex;align-items:center;gap:6px;font-family:"Oswald",sans-serif}
.logo-mark{width:16px;height:16px;background:var(--red)}
.logo-name{font-size:20px;font-weight:700;letter-spacing:1.5px;color:var(--ink);line-height:1}
.logo-sub{position:absolute;font-size:8px;letter-spacing:1px;color:var(--grey);text-transform:uppercase}
.page--front .logo{left:16px;top:520px}
.page--front .logo-sub{left:38px;top:543px}
.front-foot{position:absolute;left:0;bottom:0;width:100%;height:18px;background:var(--charcoal);border-top:3px solid var(--red)}

/* back */
.back-photo{left:190px;top:0;width:225px;height:120px;background:linear-gradient(140deg,#4a0810,#c11428 50%,#1b1c20);clip-path:polygon(18% 0,100% 0,100% 100%,0 100%)}
.page--back .logo{left:16px;top:28px}
.page--back .logo-sub{left:38px;top:51px}
.back-title{position:absolute;left:16px;top:130px;font-size:20px;width:260px}
.back-tag{position:absolute;left:0;top:182px;height:20px;width:250px;background:var(--red);color:#fff;font-family:"Oswald",sans-serif;font-weight:500;font-size:11px;line-height:20px;padding-left:16px;letter-spacing:.5px;clip-path:polygon(0 0,100% 0,94% 100%,0 100%)}
.back-intro{position:absolute;left:16px;top:214px;width:383px;font-size:9.5px;line-height:1.45;color:#333}
.props-head{position:absolute;left:16px;top:292px;font-size:20px}
.prop-list{position:absolute;left:16px;top:322px;list-style:none;font-size:10.5px;font-weight:700;line-height:1.75;text-transform:uppercase}
.prop-list li::before{content:"";display:inline-block;width:6px;height:6px;background:var(--red);margin-right:6px;vertical-align:1px}
.back-car{left:205px;top:290px;width:210px;height:190px;background:linear-gradient(150deg,#081634,var(--blue) 50%,#0a0f1c);clip-path:polygon(14% 0,100% 0,100% 100%,0 100%)}
.callout{position:absolute;left:214px;height:18px;padding:0 10px;background:var(--red);color:#fff;font-family:"Oswald",sans-serif;font-size:9.5px;line-height:18px;text-transform:uppercase;letter-spacing:.4px}
.back-foot{position:absolute;left:0;bottom:0;width:100%;height:64px;background:var(--charcoal);border-top:3px solid var(--red);color:#e6e6e6;font-size:8.5px;line-height:1.5;padding:12px 16px}
</style>
</head>
<body>

<section class="page page--front">
  <div class="photo front-hero-red" role="img" aria-label="Close-up of a glossy red luxury car body"></div>
  <div class="photo front-hero-blue" role="img" aria-label="Blue coated sports car with water beading"></div>
  <div class="photo front-stripe"></div>
  <div class="photo front-car" role="img" aria-label="Front view of a grey luxury SUV"></div>
  <div class="front-band"><h1 class="title">Functional Nano Ceramic Technology</h1></div>
  <span class="pill" style="top:392px">Aviation Borne</span>
  <span class="pill" style="top:416px">Track Proven</span>
  <h2 class="title tiers-head">Coating Tiers</h2>
  <ul class="tier-list">
    <li>1.5 Years</li><li>5 Years</li>
    <li>3 Years</li><li>10 Years</li>
  </ul>
  <div class="logo"><span class="logo-mark"></span><span class="logo-name">VELORAN</span></div>
  <span class="logo-sub">Ceramic Coating</span>
  <div class="front-foot"></div>
</section>

<section class="page page--back">
  <div class="photo back-photo" role="img" aria-label="Red sports car detail shot"></div>
  <div class="logo"><span class="logo-mark"></span><span class="logo-name">VELORAN</span></div>
  <span class="logo-sub">Ceramic Coating</span>
  <h1 class="title back-title">Functional Nano Ceramic Technology</h1>
  <div class="back-tag">AVIATION BORNE. TRACK PROVEN</div>
  <p class="back-intro">Engineered to protect the world's most exceptional vehicles, Veloran nano ceramic coatings bond directly to factory paint, forming a hard, glass-like shield. Developed from aviation surface science, each layer resists scratches, heat and chemicals while delivering a deep, lasting gloss that keeps your car showroom-ready for years.</p>
  <h2 class="title props-head">Key Properties</h2>
  <ul class="prop-list">
    <li>Scratch resistant</li>
    <li>Hydrophobic</li>
    <li>Extremely durable</li>
    <li>Heat protection up to 1200°F</li>
    <li>UV resistant</li>
    <li>Simplified maintenance</li>
    <li>Chemical resistant</li>
    <li>Deep gloss</li>
  </ul>
  <div class="photo back-car" role="img" aria-label="Blue coated sports car bonnet with water beads"></div>
  <span class="callout" style="top:440px">Superior grade protection</span>
  <span class="callout" style="top:462px">Greater gloss finish</span>
  <footer class="back-foot">
    (905) 555-0142 &nbsp;|&nbsp; hello@veloranluxe.ca &nbsp;|&nbsp; www.veloranluxe.ca<br>
    2210 Meridian Road West, Oakridge, Ontario
  </footer>
</section>

</body>
</html>
```